Redesign Business Cards, Attached

Please read instructions carefully. If you have any questions send a message before submitting your ONE design. Please redesign attached business cards. Double sided. Use same content and descriptions. Use black, silver, crimson red and gold colors. My only issue with the attached design is the background colors. I like the layout as-is. I can provide the individual pictures on the back side later. Do not submit more than one design. One submission shall include both front and back. Do not submit front and back separately. A second project will be launched to create a matching post card after completion of this.
Industry/Entity Type
see description and attachments.
Contact Information for Business Card
Requirements
Must have
- see description and attachments.
Nice to have
Should not have

```html
<!DOCTYPE html>
<html lang="en">
<head>
<meta charset="utf-8">
<title>Harborline Boat Training – Business Card</title>
<link href="https://fonts.googleapis.com/css2?family=Poppins:wght@400;500;600;700&display=swap" rel="stylesheet">
<style>
  :root {
    --stage: #ececec;
    --paper: #ffffff;
    --ink: #111111;
    --gold: #d4a51c;
    --emboss: #e8e8e8;
    --emboss-line: #d9d9d9;
    --sea-deep: #0d141d;
    --sea-mid: #2c3e50;
    --sea-light: #b7c0c8;
    --white: #ffffff;
    --badge-red: #b3192b;
    --badge-navy: #1d3b78;
  }
  * { box-sizing: border-box; margin: 0; padding: 0; }
  html, body { width: 1200px; height: 1000px; overflow: hidden; }
  body { background: var(--stage); font-family: "Poppins", sans-serif; position: relative; }

  .card { position: absolute; left: 294px; width: 613px; height: 352px; overflow: hidden; }
  .card--front { top: 134px; background: var(--paper); }
  .card--back { top: 539px; }

  /* Front */
  .service-list { position: absolute; list-style: none; }
  .service-list--left { left: 24px; top: 62px; width: 150px; }
  .service-list--right { left: 177px; top: 62px; width: 165px; }
  .service {
    position: relative; padding-left: 21px;
    font-size: 13.5px; font-weight: 600; line-height: 17px; color: var(--ink);
  }
  .service svg { position: absolute; left: 0; top: 2px; width: 13px; height: 13px; }
  .service-list--left .service:nth-child(2) { margin-top: 14px; }
  .service-list--left .service:nth-child(3) { margin-top: 16px; }
  .service-list--left .service:nth-child(4) { margin-top: 11px; }
  .service-list--right .service:nth-child(2) { margin-top: 14px; }
  .service-list--right .service:nth-child(3) { margin-top: 12px; }
  .service-list--right .service:nth-child(4) { margin-top: 11px; }

  .front-web {
    position: absolute; left: 47px; top: 295px; white-space: nowrap;
    font-size: 13.5px; font-weight: 700; color: var(--ink);
  }
  .badges { position: absolute; left: 200px; top: 274px; display: flex; gap: 10px; align-items: center; }

  .watermark { position: absolute; left: 352px; top: 16px; width: 316px; height: 316px; }
  .watermark-name {
    position: absolute; left: 420px; top: 162px;
    font-size: 22px; font-weight: 700; color: var(--emboss-line); letter-spacing: 1px;
  }

  /* Back */
  .sea-photo {
    position: absolute; inset: 0;
    background: linear-gradient(105deg, var(--sea-deep) 0%, #1a2633 40%, var(--sea-mid) 65%, var(--sea-light) 100%);
  }
  .brand-mark {
    position: absolute; left: 119px; top: 55px; width: 112px; height: 112px;
    border-radius: 50%; background: var(--ink);
    display: flex; align-items: center; justify-content: center; text-align: center;
  }
  .brand-name { font-size: 13px; font-weight: 700; color: var(--gold); line-height: 16px; width: 86px; }
  .person-name {
    position: absolute; left: 0; width: 350px; top: 180px; text-align: center;
    font-size: 21px; font-weight: 700; color: var(--gold); letter-spacing: 0.3px;
  }
  .person-title {
    position: absolute; left: 0; width: 350px; top: 208px; text-align: center;
    font-size: 11.5px; font-weight: 400; color: var(--white);
  }
  .contact-icons { position: absolute; left: 142px; top: 236px; display: flex; gap: 5px; }
  .contact-icons svg { width: 19px; height: 19px; }
  .contact-lines {
    position: absolute; left: 0; width: 350px; top: 261px; text-align: center;
    font-size: 16px; line-height: 20px; color: var(--white);
  }
  .contact-lines strong { font-weight: 700; }
</style>
</head>
<body>

<section class="card card--front" aria-label="Business card front">
  <svg class="watermark" viewBox="0 0 316 316" aria-hidden="true">
    <circle cx="158" cy="158" r="154" fill="var(--emboss)" stroke="var(--emboss-line)" stroke-width="3"/>
  </svg>
  <div class="watermark-name">HARBORLINE</div>

  <ul class="service-list service-list--left">
    <li class="service"><svg viewBox="0 0 24 24"><path fill="var(--gold)" d="M12 1l3.2 7 7.6.8-5.7 5.1 1.6 7.6L12 17.6 5.3 21.5l1.6-7.6L1.2 8.8l7.6-.8z"/></svg>Hands-On<br>Boat Training</li>
    <li class="service"><svg viewBox="0 0 24 24"><path fill="var(--gold)" d="M12 1l3.2 7 7.6.8-5.7 5.1 1.6 7.6L12 17.6 5.3 21.5l1.6-7.6L1.2 8.8l7.6-.8z"/></svg>Island Anchoring</li>
    <li class="service"><svg viewBox="0 0 24 24"><path fill="var(--gold)" d="M12 1l3.2 7 7.6.8-5.7 5.1 1.6 7.6L12 17.6 5.3 21.5l1.6-7.6L1.2 8.8l7.6-.8z"/></svg>Introduction to<br>Power Boating</li>
    <li class="service"><svg viewBox="0 0 24 24"><path fill="var(--gold)" d="M12 1l3.2 7 7.6.8-5.7 5.1 1.6 7.6L12 17.6 5.3 21.5l1.6-7.6L1.2 8.8l7.6-.8z"/></svg>Open Water<br>Advanced<br>Maneuvers</li>
  </ul>
  <ul class="service-list service-list--right">
    <li class="service"><svg viewBox="0 0 24 24"><path fill="var(--gold)" d="M12 1l3.2 7 7.6.8-5.7 5.1 1.6 7.6L12 17.6 5.3 21.5l1.6-7.6L1.2 8.8l7.6-.8z"/></svg>Precision Docking<br>&amp; Boat Handling</li>
    <li class="service"><svg viewBox="0 0 24 24"><path fill="var(--gold)" d="M12 1l3.2 7 7.6.8-5.7 5.1 1.6 7.6L12 17.6 5.3 21.5l1.6-7.6L1.2 8.8l7.6-.8z"/></svg>Coastal Navigation</li>
    <li class="service"><svg viewBox="0 0 24 24"><path fill="var(--gold)" d="M12 1l3.2 7 7.6.8-5.7 5.1 1.6 7.6L12 17.6 5.3 21.5l1.6-7.6L1.2 8.8l7.6-.8z"/></svg>Open Water<br>Boat Handling</li>
    <li class="service"><svg viewBox="0 0 24 24"><path fill="var(--gold)" d="M12 1l3.2 7 7.6.8-5.7 5.1 1.6 7.6L12 17.6 5.3 21.5l1.6-7.6L1.2 8.8l7.6-.8z"/></svg>Captaining/<br>Piloting Service<br>for Your Outings</li>
  </ul>

  <div class="front-web">HarborlineBT.com</div>
  <div class="badges">
    <svg width="56" height="56" viewBox="0 0 56 56" role="img" aria-label="Verified business badge"><circle cx="28" cy="28" r="26" fill="var(--badge-red)"/></svg>
    <svg width="52" height="60" viewBox="0 0 52 60" role="img" aria-label="Safe boating instructor badge"><rect x="4" y="4" width="44" height="52" rx="6" fill="var(--badge-navy)"/></svg>
  </div>
</section>

<section class="card card--back" aria-label="Business card back">
  <div class="sea-photo" role="img" aria-label="Aerial photo of a white center-console boat cruising across sparkling water"></div>

  <div class="brand-mark"><span class="brand-name">Harborline Boat Training</span></div>
  <div class="person-name">DANA R. WHITCOMBE</div>
  <div class="person-title">USCG LICENSED CAPTAIN CERTIFIED INSTRUCTOR</div>

  <div class="contact-icons">
    <svg viewBox="0 0 20 20" aria-label="Phone"><circle cx="10" cy="10" r="10" fill="var(--gold)"/><path d="M7 5.5l1.6 2.2-1 1.1c.7 1.3 1.6 2.2 2.9 2.9l1.1-1 2.2 1.6-.8 1.6c-3.8-.3-6.9-3.4-7.2-7.2z" fill="var(--ink)"/></svg>
    <svg viewBox="0 0 20 20" aria-label="Email"><circle cx="10" cy="10" r="10" fill="var(--gold)"/><rect x="5" y="6.5" width="10" height="7" rx="1" fill="none" stroke="var(--ink)" stroke-width="1.3"/><path d="M5.3 7l4.7 3.6L14.7 7" fill="none" stroke="var(--ink)" stroke-width="1.3"/></svg>
    <svg viewBox="0 0 20 20" aria-label="Website"><circle cx="10" cy="10" r="10" fill="var(--gold)"/><circle cx="10" cy="10" r="5" fill="none" stroke="var(--ink)" stroke-width="1.2"/><ellipse cx="10" cy="10" rx="2.2" ry="5" fill="none" stroke="var(--ink)" stroke-width="1.1"/><path d="M5 10h10" stroke="var(--ink)" stroke-width="1.1"/></svg>
  </div>

  <div class="contact-lines">
    <div><strong>Text</strong> (555) 014-2290</div>
    <div>hello@harborlinebt.com</div>
    <div>harborlinebt.com</div>
  </div>
</section>

</body>
</html>
```